I need a logo design and a business card design for a new strategy consultancy that I set up called Tessaron LLC. We help clients make strategically important decisions, cutting through the cloud of noise. The design should imply clarity, simplicity and wisdom.

```html
<!DOCTYPE html>
<html lang="en">
<head>
<meta charset="utf-8">
<title>Tessaron LLC – Business Card</title>
<link rel="stylesheet" href="https://fonts.googleapis.com/css2?family=Open+Sans:wght@400&display=swap">
<style>
  :root {
    --backdrop: #818285;
    --card-dark: #000000;
    --card-blue: #00adee;
    --ink-light: #ffffff;
  }
  html, body {
    margin: 0;
    padding: 0;
    width: 1200px;
    height: 1200px;
    overflow: hidden;
    background: var(--backdrop);
  }
  .business-card {
    position: absolute;
    left: 44px;
    top: 290px;
    width: 1098px;
    height: 628px;
    display: block;
  }
  .card-top { fill: var(--card-dark); }
  .card-bottom { fill: var(--card-blue); }
  .divider-line {
    stroke: var(--ink-light);
    stroke-width: 12;
    fill: none;
  }
  .field-label,
  .brand-name {
    font-family: "Open Sans", sans-serif;
    font-weight: 400;
    fill: var(--ink-light);
  }
  .field-label { font-size: 28px; }
  .brand-name { font-size: 62px; letter-spacing: 2px; }
  .fill-in-rule {
    stroke: var(--ink-light);
    stroke-width: 2;
  }
</style>
</head>
<body>
  <svg class="business-card" viewBox="0 0 1098 628" xmlns="http://www.w3.org/2000/svg" role="img" aria-label="Tessaron LLC business card">
    <rect class="card-top" x="0" y="0" width="1098" height="628"/>
    <polygon class="card-bottom" points="0,311 1098,295 1098,628 0,628"/>
    <line class="divider-line" x1="0" y1="311" x2="1098" y2="295"/>

    <text class="field-label name-label" x="331" y="125">NAME</text>
    <line class="fill-in-rule" x1="431" y1="128" x2="778" y2="128"/>

    <text class="brand-name" x="584" y="278" text-anchor="middle">TESSARON LLC</text>

    <g class="contact-fields">
      <text class="field-label" x="34" y="491">ADDRESS</text>
      <line class="fill-in-rule" x1="180" y1="494" x2="546" y2="494"/>
      <line class="fill-in-rule" x1="34" y1="537" x2="540" y2="537"/>
      <text class="field-label" x="34" y="576">MOBILE NO</text>
      <line class="fill-in-rule" x1="209" y1="579" x2="540" y2="579"/>
    </g>
  </svg>
</body>
</html>
```